Hi I need a website for an audio visual company called "Talvo"

We supply and install all types of technology within the very high end London residential market this includes cinemas, distributed audio (music in principle rooms) TVs, WiFi, security (video entry, CCTV, Intruder alarms), Mood lighting (kerriva), electric window treatments (curtains and blinds)
similar companies....https://fenstock.co.uk/#fenstock
https://www.wexmoor.co.uk/

```html
<!DOCTYPE html>
<html lang="en">
<head>
<meta charset="utf-8">
<title>Talvo — Smart home solutions</title>
<link href="https://fonts.googleapis.com/css2?family=Jost:wght@300;400;500&display=swap" rel="stylesheet">
<style>
:root{
  --bronze:#c18e62;
  --bronze-dark:#a8743f;
  --cream:#fbf7ee;
  --ink:#1b1b1b;
  --footer:#1e1e1e;
  --white:#ffffff;
  --muted:#cfcfcf;
  --line:#d9b690;
}
*{box-sizing:border-box;margin:0;padding:0}
html,body{width:1200px;height:3674px;overflow:hidden}
body{font-family:"Jost",Arial,sans-serif;color:var(--ink);background:var(--white);position:relative}
section,header,footer{position:absolute;left:0;width:1200px}
.abs{position:absolute}

/* buttons with corner notches */
.btn{position:absolute;display:flex;align-items:center;justify-content:center;gap:6px;font-size:11px;font-weight:500;text-decoration:none}
.btn::before,.btn::after{content:"";position:absolute;width:0;height:0}
.btn::before{top:0;left:0;border-top:12px solid currentColor;border-right:12px solid transparent}
.btn::after{bottom:0;right:0;border-bottom:12px solid currentColor;border-left:12px solid transparent}
.btn-dark{background:#2a2622;color:var(--white);border:1px solid #2a2622}
.btn-dark::before,.btn-dark::after{border-top-color:var(--bronze);border-bottom-color:var(--bronze)}
.btn-outline{border:1.5px solid currentColor;color:var(--bronze)}
.btn-outline-dark{border:1.5px solid var(--ink);color:var(--ink)}

/* wordmark */
.wordmark{display:flex;align-items:center;gap:14px;color:var(--white);font-weight:300;letter-spacing:12px}
.wordmark .mark{width:26px;height:26px;background:var(--bronze)}

/* hero */
.hero{top:0;height:675px;background:linear-gradient(180deg,#3d4451 0%,#5a6272 35%,#7d7f84 60%,#4a4a43 80%,#2f3a2a 100%)}
.hero-photo{position:absolute;inset:0;background:linear-gradient(180deg,rgba(40,46,58,.6) 0%,rgba(0,0,0,0) 40%),linear-gradient(90deg,rgba(0,0,0,0) 10%,#6b625a 40%,#8a8e95 65%,#5a5e66 90%)}
.nav{position:absolute;top:32px;left:0;width:1200px;height:70px}
.nav .wordmark{position:absolute;left:60px;top:14px;font-size:34px}
.nav-links{position:absolute;left:542px;top:42px;display:flex;gap:26px;font-size:10.5px;color:var(--white)}
.nav-links .active{color:var(--bronze)}
.nav-phone{position:absolute;left:893px;top:42px;font-size:10.5px;color:var(--white);display:flex;gap:5px;align-items:center}
.nav .quote{left:1025px;top:32px;width:112px;height:35px;background:var(--bronze);color:var(--white);border:none}
.nav .quote::before,.nav .quote::after{display:none}
.hero h1{position:absolute;left:199px;top:176px;font-size:60px;font-weight:400;color:var(--white);letter-spacing:.5px}
.hero p{position:absolute;left:200px;top:262px;font-size:13px;line-height:22px;color:var(--white);font-weight:300}
.hero .btn{left:200px;top:330px;width:112px;height:36px}

/* about */
.about{top:675px;height:594px}
.about-text{position:absolute;left:0;top:0;width:712px;height:594px;background:var(--bronze)}
.about-photo{position:absolute;left:712px;top:0;width:488px;height:594px;background:linear-gradient(180deg,#e9e6e2 0%,#d7cfc4 35%,#8a6a4e 60%,#8d7a68 78%,#b78945 100%)}
.eyebrow{font-size:12px;font-weight:500}
.about .eyebrow{position:absolute;left:62px;top:132px}
.about h2{position:absolute;left:62px;top:163px;font-size:30px;font-weight:400;line-height:37px;width:560px}
.about p{position:absolute;left:62px;top:302px;width:600px;font-size:9.5px;line-height:20px}
.about .btn{left:62px;top:421px;width:113px;height:38px}

/* services */
.services{top:1269px;height:776px;background:var(--cream)}
.svc{position:absolute;left:63px;width:92px;height:92px;border-radius:50%;background:var(--white);box-shadow:0 2px 8px rgba(0,0,0,.05);display:flex;flex-direction:column;align-items:center;justify-content:center;gap:5px;font-size:10px;text-align:center;line-height:12px}
.svc.selected{background:#f6d8bf}
.svc svg{width:22px;height:22px;stroke:var(--ink);fill:none;stroke-width:1.3}
.svc-photo{position:absolute;left:244px;top:122px;width:344px;height:531px;background:linear-gradient(90deg,#c9bfb2 0%,#e5e2de 30%,#cfd3d8 55%,#9aa3ad 75%,#6e5440 100%)}
.services .heading{position:absolute;left:663px;top:73px;font-size:22px;font-weight:400}
.services .rule{position:absolute;left:818px;top:90px;width:320px;height:1px;background:var(--line)}
.services .eyebrow{position:absolute;left:663px;top:245px;color:var(--bronze);font-weight:400}
.services h3{position:absolute;left:663px;top:273px;font-size:33px;font-weight:400;line-height:37px}
.services p{position:absolute;left:663px;top:363px;width:450px;font-size:12px;line-height:25px}
.services .btn{left:663px;top:491px;width:100px;height:37px;font-size:10px}

/* projects */
.projects{top:2045px;height:562px;background:radial-gradient(ellipse at 55% 30%,#6f8a86 0%,#3f4a48 30%,#2a2624 60%,#1c1a19 100%)}
.projects .eyebrow{position:absolute;left:200px;top:150px;color:var(--bronze);font-weight:400}
.projects h3{position:absolute;left:200px;top:180px;font-size:38px;font-weight:400;line-height:43px;color:var(--white)}
.projects p{position:absolute;left:200px;top:285px;width:400px;font-size:11px;line-height:22px;color:var(--white);font-weight:300}
.projects .link{position:absolute;left:200px;top:397px;font-size:11px;color:var(--bronze);font-weight:500}
.dots{position:absolute;left:1129px;top:246px;display:flex;flex-direction:column;gap:9px}
.dots span{width:9px;height:9px;border-radius:50%;background:var(--white)}
.dots span.on{background:var(--bronze)}

/* feed */
.feed{top:2607px;height:743px;background:var(--white)}
.feed .eyebrow{position:absolute;left:0;width:1200px;top:74px;text-align:center;color:var(--bronze);font-weight:400}
.feed-handle{position:absolute;left:0;width:1200px;top:100px;display:flex;justify-content:center;align-items:center;gap:20px;font-size:33px}
.feed-handle .sq{width:26px;height:26px;background:var(--bronze)}
.grid{position:absolute;left:63px;top:173px;display:grid;grid-template-columns:repeat(5,210px);grid-auto-rows:210px;gap:6px}
.grid div{width:210px;height:210px}
.feed .btn{left:531px;top:631px;width:138px;height:36px;font-size:10px;font-weight:400}

/* footer */
.site-footer{top:3350px;height:324px;background:var(--footer);color:var(--white)}
.site-footer .wordmark{position:absolute;left:198px;top:82px;font-size:40px;letter-spacing:14px}
.site-footer .wordmark .mark{width:34px;height:34px}
.site-footer h4{font-size:15px;font-weight:400;margin-bottom:18px}
.contact{position:absolute;left:506px;top:73px;font-size:11.5px}
.contact li{list-style:none;display:flex;gap:8px;margin-bottom:18px;line-height:18px}
.contact svg{width:10px;height:10px;flex:none;margin-top:4px;fill:var(--bronze)}
.quick{position:absolute;left:794px;top:73px;font-size:11.5px}
.quick li{list-style:none;margin-bottom:8px}
.social{position:absolute;left:970px;top:82px;display:flex;flex-direction:column;gap:8px}
.social span{width:30px;height:30px;border-radius:50%;background:#3a3a3a;display:block}
.social span.on{background:var(--bronze)}
.site-footer .divider{position:absolute;left:200px;top:270px;width:800px;height:1px;background:#3c3c3c}
.copy{position:absolute;left:0;width:1200px;top:290px;text-align:center;font-size:10.5px}
.copy b{color:var(--bronze);font-weight:400}
</style>
</head>
<body>

<header class="hero">
  <div class="hero-photo" role="img" aria-label="Photograph of a modern two-storey concrete and timber villa at dusk"></div>
  <nav class="nav">
    <div class="wordmark"><span class="mark"></span>TALVO</div>
    <div class="nav-links">
      <span class="active">Home</span><span>About us</span><span>Services</span><span>Projects</span><span>Contact Us</span>
    </div>
    <div class="nav-phone">
      <svg width="9" height="9" viewBox="0 0 24 24" fill="#fff"><path d="M6.6 10.8a15 15 0 0 0 6.6 6.6l2.2-2.2a1 1 0 0 1 1-.25 11 11 0 0 0 3.6.6 1 1 0 0 1 1 1V20a1 1 0 0 1-1 1A17 17 0 0 1 3 4a1 1 0 0 1 1-1h3.5a1 1 0 0 1 1 1c0 1.25.2 2.45.6 3.6a1 1 0 0 1-.25 1z"/></svg>
      123-456-7890
    </div>
    <a class="btn quote">Get a Quote →</a>
  </nav>
  <h1>Smart home solutions</h1>
  <p>Lorem Ipsum is simply dummy text of the printing and typesetting industry.<br>Lorem Ipsum has been the industry's standard dummy</p>
  <a class="btn btn-dark">Get a Quote →</a>
</header>

<section class="about">
  <div class="about-text">
    <div class="eyebrow">About us</div>
    <h2>We supply and install all types of technology within the very high-end london residential market</h2>
    <p>It is a long established fact that a reader will be distracted by the readable content of a page when looking at its layout. The point of using Lorem Ipsum is that it has a more-or-less normal distribution of letters, as opposed to using 'Content here, content here', making it look like readable English. Many desktop publishing packages and web page editors now use Lorem Ipsum as their default model text, and a search for 'lorem ipsum' will uncover many web sites still in their infancy...</p>
    <a class="btn btn-outline-dark">Explore more →</a>
  </div>
  <div class="about-photo" role="img" aria-label="Photograph of a luxury living room with a grey sofa, marble coffee table and warm ceiling lighting"></div>
</section>

<section class="services">
  <div class="svc" style="top:76px"><svg viewBox="0 0 24 24"><rect x="3" y="5" width="18" height="12"/><path d="M10 9l4 2-4 2z"/><path d="M8 20h8"/></svg>Cinemas</div>
  <div class="svc" style="top:182px"><svg viewBox="0 0 24 24"><path d="M4 10v4M8 7v10M12 4v16M16 7v10M20 10v4"/></svg>Distributed<br>audio</div>
  <div class="svc selected" style="top:288px"><svg viewBox="0 0 24 24"><rect x="7" y="3" width="10" height="18" rx="1"/><circle cx="12" cy="15" r="2"/><path d="M10 7h4M10 10h4"/></svg>Security</div>
  <div class="svc" style="top:394px"><svg viewBox="0 0 24 24"><circle cx="12" cy="12" r="4"/><path d="M12 3v3M12 18v3M3 12h3M18 12h3M5.6 5.6l2 2M16.4 16.4l2 2M5.6 18.4l2-2M16.4 7.6l2-2"/></svg>Mood lighting</div>
  <div class="svc" style="top:500px"><svg viewBox="0 0 24 24"><path d="M3 9a13 13 0 0 1 18 0M6 12.5a8.5 8.5 0 0 1 12 0M9 16a4 4 0 0 1 6 0"/><circle cx="12" cy="19" r="1"/></svg>WiFi</div>
  <div class="svc" style="top:606px"><svg viewBox="0 0 24 24"><rect x="4" y="3" width="16" height="18"/><path d="M4 7h16M4 11h16M4 15h16M9 3v18M15 3v18"/></svg>Electric window<br>treatments</div>

  <div class="svc-photo" role="img" aria-label="Photograph of a smart keypad door lock with a blue illuminated panel"></div>

  <h2 class="heading">Our services</h2>
  <div class="rule"></div>
  <div class="eyebrow">Security</div>
  <h3>Video entry, cctv, and<br>intruder alarms</h3>
  <p>It is a long established fact that a reader will be distracted by the readable content of a page when looking at its layout. the point of using lorem ipsum is that it has a more-or-less normal distribution of letters, as opposed to using 'content here...</p>
  <a class="btn btn-outline">Read more →</a>
</section>

<section class="projects" role="img" aria-label="Photograph of a dark home cinema room with a large screen, speakers and green sofas">
  <div class="eyebrow">Projects</div>
  <h3>Lorem ipsum luxury<br>townhouse</h3>
  <p>It is a long established fact that a reader will be distracted by readable content of a page when looking at its layout. the point of using lorem ipsum is that it has a more-or-less normal ipsum distribution letters, as opposed to using 'content here...</p>
  <div class="link">View project →</div>
  <div class="dots"><span></span><span class="on"></span><span></span><span></span><span></span></div>
</section>

<section class="feed">
  <div class="eyebrow">Snapfeed</div>
  <div class="feed-handle"><span class="sq"></span>talvo_audio_visual</div>
  <div class="grid">
    <div role="img" aria-label="Modern white house exterior" style="background:linear-gradient(180deg,#c9d4e0,#7f7a72 70%,#5b5f62)"></div>
    <div role="img" aria-label="Bright living room with pendant lamp" style="background:linear-gradient(160deg,#efe8dc,#cdbfa9)"></div>
    <div role="img" aria-label="Modern house lit at dusk" style="background:linear-gradient(180deg,#6e7d94,#3c3a3a 60%,#c48a4a)"></div>
    <div role="img" aria-label="Living room with wall-mounted television" style="background:linear-gradient(180deg,#d8c2a6,#b89b7c)"></div>
    <div role="img" aria-label="Hand touching a wall control panel" style="background:linear-gradient(160deg,#f3ece6,#d7c3b7)"></div>
    <div role="img" aria-label="Hands holding a tablet showing a room" style="background:linear-gradient(120deg,#6e1e2c,#9b8f86 55%,#d8d3cd)"></div>
    <div role="img" aria-label="Finger pressing a smart home speaker" style="background:linear-gradient(180deg,#8e8e8c,#c9c7c3)"></div>
    <div role="img" aria-label="Hand using a video entry keypad" style="background:linear-gradient(120deg,#5b7a4a,#cdd2d4 50%,#3a3d40)"></div>
    <div role="img" aria-label="Open plan kitchen and lounge with warm lighting" style="background:linear-gradient(180deg,#b18a5c,#6e5740 60%,#9c9189)"></div>
    <div role="img" aria-label="Lounge with large television and ceiling lights" style="background:linear-gradient(180deg,#efe6d8,#8a7d6e 55%,#7f8a96)"></div>
  </div>
  <a class="btn btn-outline">Follow on snapfeed →</a>
</section>

<footer class="site-footer">
  <div class="wordmark"><span class="mark"></span>TALVO</div>
  <div class="contact">
    <h4>Contact us</h4>
    <ul>
      <li><svg viewBox="0 0 24 24"><path d="M6.6 10.8a15 15 0 0 0 6.6 6.6l2.2-2.2a1 1 0 0 1 1-.25 11 11 0 0 0 3.6.6 1 1 0 0 1 1 1V20a1 1 0 0 1-1 1A17 17 0 0 1 3 4a1 1 0 0 1 1-1h3.5a1 1 0 0 1 1 1c0 1.25.2 2.45.6 3.6a1 1 0 0 1-.25 1z"/></svg>123.456.7890</li>
      <li><svg viewBox="0 0 24 24"><path d="M2 5h20v14H2z M2 5l10 8 10-8"/></svg>info@talvoaudiovisual.com</li>
      <li><svg viewBox="0 0 24 24"><path d="M12 2a7 7 0 0 0-7 7c0 5 7 13 7 13s7-8 7-13a7 7 0 0 0-7-7zm0 9.5A2.5 2.5 0 1 1 12 6.5a2.5 2.5 0 0 1 0 5z"/></svg>505 E Lorem Street, # Ipsum, work<br>MH 33602</li>
    </ul>
  </div>
  <div class="quick">
    <h4>Quick links</h4>
    <ul><li>Home</li><li>About Us</li><li>Services</li><li>Projects</li><li>Contact Us</li></ul>
  </div>
  <div class="social"><span></span><span class="on"></span><span></span><span></span></div>
  <div class="divider"></div>
  <div class="copy">© 2024 <b>Talvo Audio Visual</b> — All rights reserved</div>
</footer>

</body>
</html>
```